Pelbrook Business Cards

Create new business cards with the details below.

Aaron Velst
Director

MB: +61 412 563 904
PH: 1300 417 639
Email: aaron.velst@pelbrook.com.au
Address: 27C Marlow Parade, Ashbury Vale VIC 3099 Australia
Website: www.pelbrook.com.au

Target Market(s)

Other business

Industry/Entity Type

Business

Requirements
Must have
• must be clean looking

```html
<!DOCTYPE html>
<html lang="en">
<head>
<meta charset="utf-8">
<title>Pelbrook Business Cards</title>
<link href="https://fonts.googleapis.com/css2?family=Montserrat:wght@700&family=Arimo:wght@400&family=Dosis:wght@300&family=Signika:wght@700&display=swap" rel="stylesheet">
<style>
  :root {
    --stage: #4a4747;
    --cream: #fcf5e4;
    --sand: #dfd6bf;
    --line-green: #66773a;
    --brand-green: #8cc63f;
    --ink: #1e1c1a;
    --photo-dark: #3c3f44;
    --photo-light: #c9ced3;
  }
  * { box-sizing: border-box; margin: 0; padding: 0; }
  html, body { width: 1200px; height: 1200px; overflow: hidden; }
  body { background: var(--stage); position: relative; font-family: "Arimo", Arial, sans-serif; }

  .card {
    position: absolute; left: 150px; width: 900px; height: 514px;
    background: var(--cream); overflow: hidden;
    box-shadow: 0 10px 24px rgba(0,0,0,.35);
  }
  .card--front { top: 58px; }
  .card--back  { top: 628px; }

  .band {
    position: absolute; left: 0; right: 0; background: var(--sand);
  }
  .band::before, .band::after {
    content: ""; position: absolute; left: 0; right: 0; height: 4px;
    background: var(--line-green); box-shadow: 0 3px 6px rgba(60,70,30,.35);
  }
  .band::before { top: -4px; }
  .band::after  { bottom: -4px; }
  .card--front .band { top: 196px; height: 238px; }
  .card--back .band { top: 0; height: 300px; }
  .card--back .band::before { display: none; }

  .brand {
    position: absolute; display: flex; align-items: center; gap: 16px;
  }
  .brand__mark { width: 30px; height: 30px; background: var(--brand-green); }
  .brand__name {
    font-family: "Montserrat", Arial, sans-serif; font-weight: 700;
    font-size: 58px; letter-spacing: 1px; color: var(--brand-green); line-height: 1;
  }
  .card--front .brand { left: 185px; top: 92px; }
  .card--back .brand { right: 70px; top: 340px; }

  .photo {
    position: absolute; right: 110px; top: 160px; width: 300px; height: 232px;
    background: linear-gradient(180deg, var(--photo-light) 0%, #9aa1a8 55%, var(--photo-dark) 100%);
  }

  .tagline {
    position: absolute; left: 50px; bottom: 18px;
    font-family: "Dosis", sans-serif; font-weight: 300;
    font-size: 30px; letter-spacing: 3px; color: var(--ink);
  }

  .contact { position: absolute; left: 100px; top: 92px; color: var(--ink); }
  .contact__name {
    font-family: "Signika", sans-serif; font-weight: 700;
    font-size: 25px; letter-spacing: 1.5px; margin-bottom: 8px;
  }
  .contact__role, .contact__item { font-size: 21px; line-height: 30px; }
  .contact__item { display: flex; align-items: center; gap: 4px; }
  .contact__item svg { width: 24px; height: 20px; flex: none; }

  .website {
    position: absolute; right: 72px; top: 418px;
    font-size: 25px; letter-spacing: 1px; color: var(--ink);
  }
</style>
</head>
<body>

<section class="card card--front">
  <div class="band"></div>
  <div class="brand">
    <span class="brand__mark"></span>
    <span class="brand__name">PELBROOK</span>
  </div>
  <div class="photo" role="img" aria-label="Photo of a bright room with a large arched window fitted with white plantation shutters"></div>
  <p class="tagline">CUSTOM DESIGNED QUALITY SHUTTERS</p>
</section>

<section class="card card--back">
  <div class="band"></div>
  <div class="contact">
    <p class="contact__name">AARON VELST</p>
    <p class="contact__role">Director</p>
    <p class="contact__item">
      <svg viewBox="0 0 24 20" aria-hidden="true"><path d="M2 6 Q12 0 22 6 L20 9 L16 8 L16 6 Q12 4.5 8 6 L8 8 L4 9 Z" fill="#2a2624"/><rect x="5" y="10" width="14" height="9" rx="2" fill="#2a2624"/></svg>
      1300.417.639
    </p>
    <p class="contact__item">
      <svg viewBox="0 0 24 20" aria-hidden="true"><rect x="2" y="3" width="20" height="14" fill="none" stroke="#2a2624" stroke-width="1.4"/><path d="M2 3 L12 11 L22 3 M2 17 L9 9 M22 17 L15 9" fill="none" stroke="#2a2624" stroke-width="1.2"/></svg>
      aaron.velst@pelbrook.com.au
    </p>
    <p class="contact__item">
      <svg viewBox="0 0 24 20" aria-hidden="true"><path d="M2 3 L22 3 L12 19 Z" fill="#3a2a20"/></svg>
      27C Marlow Parade, Ashbury Vale VIC 3099 Australia
    </p>
  </div>
  <div class="brand">
    <span class="brand__mark"></span>
    <span class="brand__name">PELBROOK</span>
  </div>
  <p class="website">WWW.PELBROOK.COM.AU</p>
</section>

</body>
</html>
```